Marketing Flyer for Ashford Ridge Storage Climate Control Units

We are looking for a professional looking Marketing Flyer to advertise for our Climate Control Self Storage Units. Incorporate photos and our LOGO into the marketing flyer. See our website: AshfordRidgestorage.example
Updates

Marketing Flyer for our Self Storage Climate Control Units at Ashford Ridge Storage in Waynesville, NC

Want more designers to have a chance to submit entries.

Target Market(s)

Self Storage Facility Renters

Industry/Entity Type

Self Storage Facility

Font styles to use
Other font styles liked:
• Montserrat Font is what was used for our LOGO and would like to maintain consistency of Font on the Flyer

Colors
0054AA
0677BA
7BADD7
CADEEF
E8F1F8

Requirements
Must have
• Need to have LOGO in the Flyer and photos of the Climate Control Units

```html
<!DOCTYPE html>
<html lang="en">
<head>
<meta charset="utf-8">
<title>Ashford Ridge Storage – Climate Control Units Flyer</title>
<link href="https://fonts.googleapis.com/css2?family=Montserrat:ital,wght@0,400;0,500;0,700;0,800;0,900;1,700&display=swap" rel="stylesheet">
<style>
  :root{
    --navy:#1a1a66;
    --navy-deep:#14144f;
    --blue:#0677BA;
    --blue-strong:#0054AA;
    --blue-soft:#7BADD7;
    --blue-pale:#CADEEF;
    --panel:#eff0f4;
    --white:#ffffff;
    --ink:#1b1b5e;
    --stage:#d9dadd;
  }
  *{margin:0;padding:0;box-sizing:border-box}
  html,body{width:742px;height:1200px;overflow:hidden;background:var(--stage);font-family:'Montserrat',sans-serif}
  .flyer-wrap{position:absolute;left:0;top:75px;width:742px;height:1050px;overflow:hidden}
  .flyer{position:absolute;left:0;top:0;width:879px;height:1244px;background:var(--white);transform:scale(0.8441);transform-origin:0 0;overflow:hidden}
  .hero-art{position:absolute;left:0;top:0;width:879px;height:620px}
  .brand{position:absolute;left:68px;top:48px;display:flex;align-items:center;gap:22px;color:var(--white)}
  .brand-mark{width:66px;height:66px;border:5px solid var(--white);border-radius:6px}
  .brand-name{font-weight:500;line-height:1.05}
  .brand-name .line1{display:block;font-size:27px;letter-spacing:.5px}
  .brand-name .line2{display:block;font-size:17px;letter-spacing:5px;text-align:center;margin-top:4px}
  .headline{position:absolute;left:112px;top:172px;color:var(--white);font-weight:900;font-size:50px;line-height:49px;letter-spacing:.5px;text-transform:uppercase}
  .units-panel{position:absolute;left:73px;top:630px;width:734px;height:446px;background:var(--panel);border-radius:26px}
  .unit-art{position:absolute;border-radius:4px}
  .unit-art.small{left:150px;top:550px;width:160px;height:150px;background:linear-gradient(150deg,#f4f4f4 0%,#c9c9cc 60%,#8e8e93 100%)}
  .unit-art.medium{left:580px;top:558px;width:162px;height:160px;background:linear-gradient(150deg,#f2f2f3 0%,#c5c6c9 60%,#8a8b90 100%)}
  .lock-art{position:absolute;left:378px;top:668px;width:118px;height:408px;border-radius:50px 50px 8px 8px;background:linear-gradient(180deg,#4a7fc0 0%,var(--blue-strong) 45%,#2b3e73 100%)}
  .size-tab{position:absolute;width:33px;height:118px;background:var(--blue);border-radius:6px;color:var(--white);font-size:17px;font-weight:400;letter-spacing:1px;display:flex;align-items:center;justify-content:center}
  .size-tab span{white-space:nowrap}
  .size-tab.small{left:40px;top:795px}
  .size-tab.small span{transform:rotate(-90deg)}
  .size-tab.medium{left:808px;top:795px}
  .size-tab.medium span{transform:rotate(90deg)}
  .size-list{position:absolute;color:var(--ink);font-weight:800;font-size:49px;line-height:65px;letter-spacing:-.5px}
  .size-list.small{left:114px;top:724px}
  .size-list.medium{left:544px;top:740px}
  .features{position:absolute;list-style:none;color:var(--ink);font-size:22px;font-weight:400}
  .features li{display:flex;align-items:flex-start;gap:16px;margin-bottom:12px;line-height:26px}
  .features svg{flex:none;width:30px;height:30px;margin-top:-2px}
  .features.small{left:114px;top:939px}
  .features.medium{left:544px;top:897px}
  .footer{position:absolute;left:0;top:1090px;width:879px;height:154px;background:var(--navy)}
  .footer-review{position:absolute;right:0;top:0;width:460px;height:154px;background:var(--blue);clip-path:polygon(50px 0,100% 0,100% 100%,0 100%)}
  .contact{position:absolute;left:68px;top:30px;color:var(--white)}
  .contact-row{display:flex;align-items:flex-start;gap:14px}
  .contact-row svg{flex:none;width:24px;height:24px;margin-top:2px}
  .address{font-size:22px;line-height:27px;font-weight:400}
  .phone{font-size:30px;font-weight:700;margin-top:10px;align-items:center}
  .review{position:absolute;left:512px;top:30px;color:var(--white);width:340px}
  .review-head{display:flex;align-items:center;gap:20px;font-style:italic;font-weight:700;font-size:18px}
  .stars{font-style:normal;font-size:20px;letter-spacing:10px}
  .review p{font-size:18px;line-height:23px;margin-top:12px;font-weight:400}
</style>
</head>
<body>
<div class="flyer-wrap">
  <div class="flyer">
    <svg class="hero-art" viewBox="0 0 879 620" aria-hidden="false">
      <defs>
        <linearGradient id="hallway" x1="0" y1="0" x2="1" y2="1">
          <stop offset="0" stop-color="#2f4fa8"/>
          <stop offset=".5" stop-color="#d9dde6"/>
          <stop offset="1" stop-color="#1f3d98"/>
        </linearGradient>
        <linearGradient id="doors" x1="0" y1="0" x2="1" y2="0">
          <stop offset="0" stop-color="#e7e9ee"/>
          <stop offset=".35" stop-color="#2146a8"/>
          <stop offset="1" stop-color="#163a9a"/>
        </linearGradient>
      </defs>
      <path d="M0 0H879V330L300 502Q250 520 200 496L0 392Z" fill="var(--navy)"/>
      <path d="M0 390L200 494Q250 518 300 500L292 512Q248 534 196 510L0 420Z" fill="var(--blue)"/>
      <polygon role="img" aria-label="Photo of an indoor storage hallway lined with blue roll-up doors"
        points="690,35 863,135 863,335 690,435 517,335 517,135" fill="url(#hallway)" stroke="var(--white)" stroke-width="10" stroke-linejoin="round"/>
      <polygon role="img" aria-label="Photo of blue roll-up storage unit doors"
        points="565,320 686,390 686,530 565,600 444,530 444,390" fill="url(#doors)" stroke="var(--white)" stroke-width="10" stroke-linejoin="round"/>
    </svg>

    <div class="brand">
      <div class="brand-mark"></div>
      <div class="brand-name"><span class="line1">ASHFORD RIDGE</span><span class="line2">STORAGE</span></div>
    </div>

    <h1 class="headline">Climate<br>Control<br>Self<br>Storage<br>Units</h1>

    <div class="units-panel"></div>
    <div class="unit-art small" role="img" aria-label="Illustration of a small storage building with an open unit"></div>
    <div class="unit-art medium" role="img" aria-label="Illustration of a medium storage building with an open unit"></div>
    <div class="lock-art" role="img" aria-label="Illustration of a blue padlock and key"></div>

    <div class="size-tab small"><span>SMALL</span></div>
    <div class="size-tab medium"><span>MEDIUM</span></div>

    <div class="size-list small">5’ X 5’<br>5’ X 10’<br>10’ X 10’</div>
    <div class="size-list medium">10’ X 12’<br>10’ X 17’</div>

    <ul class="features small">
      <li><svg viewBox="0 0 30 30" fill="none" stroke="var(--blue)" stroke-width="2"><path d="M12 4H4V26H26V18"/><path d="M26 4L13 17M13 9V17H21"/></svg>Inside</li>
      <li><svg viewBox="0 0 30 30" fill="none" stroke="var(--blue)" stroke-width="2"><rect x="11" y="2" width="7" height="18" rx="3.5"/><circle cx="14.5" cy="23" r="5"/><path d="M5 6H9M5 10H9M5 14H9M22 6Q25 9 22 12"/></svg><span>Climate<br>Controlled</span></li>
    </ul>
    <ul class="features medium">
      <li><svg viewBox="0 0 30 30" fill="none" stroke="var(--blue)" stroke-width="2"><path d="M12 4H4V26H26V18"/><path d="M26 4L13 17M13 9V17H21"/></svg>Inside</li>
      <li><svg viewBox="0 0 30 30" fill="none" stroke="var(--blue)" stroke-width="2"><rect x="11" y="2" width="7" height="18" rx="3.5"/><circle cx="14.5" cy="23" r="5"/><path d="M5 6H9M5 10H9M5 14H9M22 6Q25 9 22 12"/></svg><span>Climate<br>Controlled</span></li>
    </ul>

    <footer class="footer">
      <div class="footer-review"></div>
      <div class="contact">
        <div class="contact-row address"><svg viewBox="0 0 24 24"><circle cx="12" cy="12" r="12" fill="var(--blue)"/><path d="M12 5a4.5 4.5 0 0 0-4.5 4.5C7.5 13 12 18 12 18s4.5-5 4.5-8.5A4.5 4.5 0 0 0 12 5z" fill="none" stroke="var(--white)" stroke-width="1.6"/><circle cx="12" cy="9.5" r="1.6" fill="var(--white)"/></svg><span>42 Linden Hollow Rd,<br>Brookfield, NC 28700</span></div>
        <div class="contact-row phone"><svg viewBox="0 0 24 24"><circle cx="12" cy="12" r="12" fill="var(--blue)"/><path d="M8.5 6.5l2 2-1.2 1.6a7 7 0 0 0 4.6 4.6l1.6-1.2 2 2-1.5 1.7c-4.6-.4-8.8-4.6-9.2-9.2z" fill="var(--white)"/></svg>(555) 014-2290</div>
      </div>
      <div class="review">
        <div class="review-head">jordanmlee <span class="stars">★★★★★</span></div>
        <p>Excellent service and wonderful space to store all of my cool stuff! Highly recommend!</p>
      </div>
    </footer>
  </div>
</div>
</body>
</html>
```